Flyer-Design für Prozessfinanzierungsfirma
Zielgruppe
Wir sind eine Prozessfinanzierungsfirma. im Versicherungsbereich die größte Österreichs mit mehr als 50.000 Klienten und unser neues Projekt ist die Prozessfinanzierung von Patienten die durch einen Kunstfehler (Fehler von Ärzten) auf Schadenersatz klagen wollen aber nicht die Finanziellen Möglichkeiten haben.
Aufgabenstellung
Folder soll eine DIN A4 Doppelseite sein (also 4 A4 Seiten)
plus extra ein A4 Einlage Blatt Fragebogen fix vorgegebene Fragen.
#604132 Dieser Folder ist für die gleiche Firma im Bereich Versicherungen
www.heilirrtum-beispiel.at. TEXTE und DESIGN - FARBEN und INHALTE von dieser Homepage übernehmen
die Seite www.schutzbrief-muster.at ist die gleiche Prozessfinanzierungsfirma - hier gibt es bereits einen Folder. Ich lade diesen hoch...
Diese Fragen sind unbedingt 1:1 zu übernehmen für das Einlageblatt :
o Was waren meine Erkrankungen vor der Behandlung, inkl. Dauermedikation?
o Warum ging ich zum Arzt?
o Was hat mir der Arzt empfohlen?
o Wurde ich über die unterschiedlichen Behandlungsmöglichkeiten aufgeklärt?
o Was wollte ich haben?
o Was wurde gemacht?
o Was hat der Arzt aus meiner Sicht falsch gemacht?
o Was wurde als weiterer Behandlungsweg empfohlen?
o Habe ich den Arzt mit meinem Problem konfrontiert?
o Wie hat mein Arzt darauf reagiert?
o Was ist jetzt genau schlechter als vorher?
Bei dem A4 Einlageblatt sollen auf der Vorderseite und der halben Rückseite diese Fragen mit entsprechendem Platz für den Text zum ausfüllen erscheinen und die untere Hälfte der 2. Seite mit einem kurzen Slogan nochmal auf unsere Leistung aufmerksam machen - ein Feld in Kreditkartengrösse für den Empfehlungsbgeber weiss zum einkleben einer Karte freibleiben und die Firmendaten (siehe Homepage) mit Anschrift, Telefonnummer und e-mailadresse angegeben sein

```html
<!DOCTYPE html>
<html lang="de">
<head>
<meta charset="utf-8">
<title>Fragebogen – Klagehilfe Nord</title>
<link rel="stylesheet" href="https://fonts.googleapis.com/css2?family=Source+Sans+3:ital,wght@0,400;0,700;0,900;1,700&display=swap">
<style>
  :root {
    --brand-red: #7f1d1d;
    --line-red: #8a3030;
    --ink: #1f1f1f;
    --logo-ink: #3b3b3b;
    --panel-grey: #eceef2;
    --field-white: #ffffff;
    --photo-light: #a9bcc3;
    --photo-mid: #8ea3ab;
    --photo-dark: #6f868f;
  }
  * { margin: 0; padding: 0; box-sizing: border-box; }
  html, body { width: 855px; height: 1200px; overflow: hidden; background: #fff; }
  body { font-family: "Source Sans 3", sans-serif; color: var(--ink); }

  .sheet { position: relative; width: 855px; height: 1200px; overflow: hidden; background: #fff; }

  .hero-photo {
    position: absolute; left: 0; top: 0; width: 855px; height: 266px;
    background: linear-gradient(135deg, var(--photo-light) 0%, var(--photo-mid) 55%, var(--photo-dark) 100%);
  }

  .brand {
    position: absolute; left: 513px; top: 165px;
    display: flex; align-items: center; gap: 12px;
  }
  .brand-square {
    width: 54px; height: 54px; border: 3px solid var(--logo-ink);
  }
  .brand-name {
    font-weight: 700; font-size: 27px; color: var(--logo-ink); letter-spacing: 0.5px;
  }

  .intro { position: absolute; left: 0; top: 266px; width: 855px; height: 129px; background: #fff; }
  .title {
    position: absolute; left: 42px; top: 12px;
    font-weight: 900; font-size: 50px; color: var(--brand-red); letter-spacing: 0.5px; line-height: 1;
  }
  .subtitle {
    position: absolute; left: 46px; top: 70px;
    font-weight: 700; font-style: italic; font-size: 19.5px; line-height: 1.2;
  }

  .questions { position: absolute; left: 0; top: 395px; width: 855px; height: 805px; background: var(--panel-grey); }
  .question { position: absolute; left: 0; width: 855px; height: 107px; }
  .question-label {
    position: absolute; left: 41px; top: 34px;
    font-size: 20.5px; line-height: 1;
  }
  .question-label::before { content: "•"; margin-right: 4px; }
  .answer-field {
    position: absolute; left: 67px; top: 71px; width: 733px; height: 74px;
    background: var(--field-white); border-radius: 0 22px 22px 0;
  }
  .answer-line {
    position: absolute; left: 5px; right: 7px; top: 35px;
    border-top: 1.4px dashed var(--line-red);
  }
</style>
</head>
<body>
<main class="sheet">
  <div class="hero-photo" role="img" aria-label="Foto: Blutdruckmessung am Arm eines Patienten, Stethoskop, Klemmbrett und Manometer auf einem Tisch"></div>
  <div class="brand">
    <span class="brand-square"></span>
    <span class="brand-name">Klagehilfe Nord</span>
  </div>

  <header class="intro">
    <h1 class="title">FRAGEBOGEN</h1>
    <p class="subtitle">Die Fragen bitte genau lesen und die Antworten so genau wie möglich formulieren.</p>
  </header>

  <section class="questions">
    <div class="question" style="top:0">
      <p class="question-label">Was waren meine Erkrankungen vor der Behandlung, inkl. Dauermedikation?</p>
      <div class="answer-field"><div class="answer-line"></div></div>
    </div>
    <div class="question" style="top:107px">
      <p class="question-label">Warum ging ich zum Arzt?</p>
      <div class="answer-field"><div class="answer-line"></div></div>
    </div>
    <div class="question" style="top:214px">
      <p class="question-label">Was hat mir der Arzt empfohlen?</p>
      <div class="answer-field"><div class="answer-line"></div></div>
    </div>
    <div class="question" style="top:321px">
      <p class="question-label">Wurde ich über die unterschiedlichen Behandlungsmöglichkeiten aufgeklärt?</p>
      <div class="answer-field"><div class="answer-line"></div></div>
    </div>
    <div class="question" style="top:428px">
      <p class="question-label">Was wollte ich haben?</p>
      <div class="answer-field"><div class="answer-line"></div></div>
    </div>
    <div class="question" style="top:535px">
      <p class="question-label">Was wurde gemacht?</p>
      <div class="answer-field"><div class="answer-line"></div></div>
    </div>
    <div class="question" style="top:642px">
      <p class="question-label">Was hat der Arzt aus meiner Sicht falsch gemacht?</p>
      <div class="answer-field"><div class="answer-line"></div></div>
    </div>
  </section>
</main>
</body>
</html>
```